Completely Coded Dog Community Website - Mobile Centric & Highly Responsive

We need a completely coded design based in Wordpress CMS that is designed with mobile in mind first! I would like to carry over the style of our current website (brightkennels.c0m) into the design of the responsive website. In addition, please only submit designs if you provide high quality admin support, as the winning design will likely be hired to provide monthly support forward at $100/month (SEO skill set valued). Also am looking for a quote on an iphone and android app so please submit designs only if you have capability to create the highest quality apps. No cheap looking template submissions please...will need form, chat, sign in and e-commerce integration. I have vector files if needed for website.
Updates

Project Deadline Extended
Reason: Want to see more mobile friendly, modern designs and responses to willingness for web admin support going forward. Thanks

Target Market(s)

Adults based in the USA aged 25-50 that own dogs

Industry/Entity Type

E-Commerce

Requirements
Must have
• Pages:
Home Page
About Us
Contact Us
Dog Deals
Videos
Photos
Health
Training
Breeds
Ask the Dog Expert
Dog Product Reviews
Dog Stories
Dog Friendly Travel
Dog Care
Contests
Nice to have
• SEO
Metatags
Unique page layouts
Social integration to our social media accounts
Social API logins
Should not have
• Cheap template look
Not consistent with previous color scheme
Different logo than our current options

```html
<!DOCTYPE html>
<html lang="en">
<head>
<meta charset="utf-8">
<title>BrightKennels — Dog Community</title>
<link href="https://fonts.googleapis.com/css2?family=Open+Sans:wght@400;600;700&family=Oswald:wght@400;500&display=swap" rel="stylesheet">
<style>
:root{
  --brown-dark:#33241a;
  --brown:#5b3f2c;
  --teal:#3c8c9e;
  --teal-dark:#2e7688;
  --orange:#f29b21;
  --grey-bg:#ebe8e3;
  --text:#3a3a3a;
  --muted:#8a8a8a;
  --line:#dcdcdc;
  --white:#fff;
}
*{box-sizing:border-box;margin:0;padding:0}
html,body{width:713px;height:1200px;overflow:hidden}
body{font-family:"Open Sans",Arial,sans-serif;color:var(--text);background:var(--white);font-size:8px;position:relative}
.wrap{width:535px;margin:0 auto;position:relative}

.topbar{height:19px;background:var(--brown-dark);color:#d9c9b9;font-size:6px;line-height:19px}
.topbar .wrap{display:flex;justify-content:space-between}
.topbar span{margin-right:9px}
.topbar .account span{margin:0 0 0 9px}
.topbar .account .signup{background:var(--orange);color:#fff;padding:0 5px}
.nav{height:21px;background:var(--brown);border-bottom:2px solid var(--orange)}
.nav ul{list-style:none;display:flex;justify-content:space-between;line-height:21px}
.nav li{color:#fff;font-size:6.4px;font-weight:700;text-transform:uppercase}
.nav li.active{color:var(--orange)}

.header{height:82px;display:flex;align-items:center}
.callbox{width:120px}
.callbox .tag{display:inline-block;background:var(--teal);color:#fff;font-size:6px;font-weight:700;padding:2px 6px;border-radius:2px}
.callbox .phone{font-family:Oswald,sans-serif;font-size:18px;color:var(--teal-dark);line-height:22px}
.agent{width:52px;height:52px;border-radius:50%;background:radial-gradient(circle at 50% 40%,#e9d1bd,#b88b6e);margin-left:-10px}
.brand{flex:1;display:flex;align-items:center;justify-content:center;gap:6px;margin-left:-20px}
.brand .dot{width:14px;height:14px;border-radius:50%;background:var(--orange)}
.brand .name{font-family:Oswald,sans-serif;font-size:24px;font-weight:500;color:var(--orange)}
.shop{width:160px}
.search{display:flex;height:16px;border:1px solid var(--line)}
.search span{flex:1;font-size:6px;color:var(--muted);line-height:14px;padding-left:5px}
.search i{width:18px;background:var(--orange)}
.cart{margin-top:6px;font-size:6px;display:flex;align-items:center;gap:4px}
.cart b{background:var(--teal);color:#fff;padding:2px 4px}

.hero{height:327px;background:linear-gradient(135deg,#cfb99f 0%,#9c7048 45%,#5c3a22 100%);position:relative}
.hero .caption{position:absolute;left:0;right:0;bottom:24px;height:70px;background:rgba(47,118,136,.92);color:#fff;text-align:center;padding-top:12px}
.hero h1{font-family:Oswald,sans-serif;font-weight:500;font-size:17px;letter-spacing:.5px}
.hero p{font-size:6px;line-height:9px;width:390px;margin:4px auto 0;color:#e3f0f3}
.dots{display:flex;justify-content:center;gap:4px}
.dots i{width:5px;height:5px;border-radius:50%;background:#9aa}
.dots i.on{background:var(--text)}
.hero .dots{position:absolute;bottom:8px;left:0;right:0}
.hero .dots i{background:#cfe2e6}
.hero .dots i.on{background:#fff}

.featured{background:var(--grey-bg);margin-top:8px;height:323px;padding-top:20px;border-top:1px solid #e0dbd3}
.section-title{font-family:Oswald,sans-serif;font-weight:400;font-size:15px;text-align:center;color:#333;letter-spacing:.5px}
.rule{width:120px;height:1px;background:#c9c2b8;margin:6px auto 14px}
.cards{display:flex;justify-content:space-between;position:relative}
.card{width:99px;background:var(--white);border:1px solid #d8d2c9;padding:4px 4px 8px;text-align:center}
.card .photo{height:78px}
.card h3{font-size:6.5px;font-weight:600;margin-top:6px}
.card p{font-size:5.5px;color:var(--muted);margin-top:2px}
.btn{display:inline-block;margin-top:5px;padding:3px 14px;font-size:6.5px;font-weight:700;color:#fff;background:var(--orange);border-radius:2px}
.btn.teal{background:var(--teal)}
.arrow{position:absolute;top:45px;width:10px;height:16px;color:#777}
.arrow.l{left:-16px}.arrow.r{right:-16px}
.featured .dots{margin-top:18px}

.columns{display:flex;justify-content:space-between;padding-top:26px;height:240px}
.col h2{font-family:Oswald,sans-serif;font-weight:500;font-size:12px;color:#333;border-bottom:1px solid var(--line);padding-bottom:5px;margin-bottom:8px}
.popular{width:115px}
.popular li{list-style:none;font-size:6px;color:var(--muted);padding:4px 0;border-bottom:1px dotted var(--line);line-height:8px}
.popular li.hot{color:var(--orange)}
.more{font-size:6px;font-weight:700;margin-top:7px;color:#555}
.news{width:150px}
.news .item{margin-bottom:8px}
.news .date{font-size:5.5px;color:var(--muted)}
.news h4{font-size:6.5px;font-weight:700}
.news p{font-size:5.5px;color:var(--muted);line-height:7.5px}
.testimonials{width:220px}
.quote{display:flex;gap:6px;margin-bottom:10px}
.quote .avatar{width:22px;height:22px;border-radius:50%;background:#c9b5a3;flex:none}
.quote p{font-size:5.5px;color:var(--muted);line-height:8px}
.quote b{display:block;font-size:5.5px;color:var(--teal-dark);margin-top:2px}

.footer{background:var(--teal);height:153px;color:#fff;padding-top:18px}
.footer .wrap{display:flex}
.fcol{width:100px}
.fcol h5{font-size:6.5px;font-weight:700;margin-bottom:5px;text-transform:uppercase}
.fcol li{list-style:none;font-size:5.5px;line-height:9px;color:#dcecef;text-transform:uppercase}
.fbrand{flex:1;text-align:right}
.fbrand .name{font-family:Oswald,sans-serif;font-size:20px;font-weight:500;color:var(--orange)}
.fbrand .call{font-size:7px;margin-top:8px}
.fbrand .call b{font-family:Oswald,sans-serif;font-size:17px;font-weight:400;margin-left:4px}
.social{display:flex;justify-content:flex-end;gap:5px;margin-top:8px}
.social i{width:14px;height:14px;border-radius:50%;background:#fff;opacity:.9}
.bottombar{height:27px;background:var(--brown-dark);color:#bfae9c;font-size:6px;text-align:center;line-height:27px}
</style>
</head>
<body>
<div class="topbar"><div class="wrap">
  <div><span>WELCOME</span><span>CONTESTS</span><span>DOG FRIENDLY TRAVEL</span><span>CONTACT US</span></div>
  <div class="account"><span>LOGIN</span><span class="signup">SIGN UP</span><span>DOG STORIES</span></div>
</div></div>
<nav class="nav"><div class="wrap"><ul>
  <li class="active">Home</li><li>About Us</li><li>Dog Deals</li><li>Videos</li><li>Photos</li><li>Health</li><li>Training</li><li>Breeds</li><li>Ask the Dog Expert</li><li>Dog Product Reviews</li><li>Dog Stories</li>
</ul></div></nav>

<header class="header wrap">
  <div class="callbox"><span class="tag">CALL US NOW!</span><div class="phone">555 014 2290</div></div>
  <div class="agent" role="img" aria-label="Portrait of a support agent with headset"></div>
  <div class="brand"><span class="dot"></span><span class="name">BrightKennels</span></div>
  <div class="shop">
    <div class="search"><span>Search</span><i></i></div>
    <div class="cart"><b>Cart</b> 0 ITEMS $0.00</div>
  </div>
</header>

<section class="hero wrap" role="img" aria-label="Woman smiling while hugging her brown dog">
  <div class="caption">
    <h1>LET TRUE FRIENDSHIP INTO YOUR LIFE!</h1>
    <p>Join our community of dog lovers to share stories, photos, training tips and health advice, and find great deals on everything your best friend needs to live a happy life.</p>
  </div>
  <div class="dots"><i class="on"></i><i></i><i></i><i></i></div>
</section>

<section class="featured">
  <div class="wrap">
    <h2 class="section-title">FEATURED PUPPIES</h2>
    <div class="rule"></div>
    <div class="cards">
      <svg class="arrow l" viewBox="0 0 10 16"><path d="M8 1L2 8l6 7" fill="none" stroke="currentColor" stroke-width="2"/></svg>
      <div class="card"><div class="photo" role="img" aria-label="Golden retriever puppy" style="background:linear-gradient(#e8d3ae,#c99a5c)"></div><h3>Lorem ipsum dolor sit</h3><p>Short puppy bio text here</p><span class="btn">VOTE NOW</span></div>
      <div class="card"><div class="photo" role="img" aria-label="Cream puppy lying down" style="background:linear-gradient(#efe4d2,#cdb18a)"></div><h3>Lorem ipsum dolor sit</h3><p>Short puppy bio text here</p><span class="btn teal">VOTE NOW</span></div>
      <div class="card"><div class="photo" role="img" aria-label="Labrador puppy sitting" style="background:linear-gradient(#f1e6d6,#c49a6a)"></div><h3>Lorem ipsum dolor sit</h3><p>Short puppy bio text here</p><span class="btn">VOTE NOW</span></div>
      <div class="card"><div class="photo" role="img" aria-label="Pug puppy" style="background:linear-gradient(#c9b9a4,#6e5a48)"></div><h3>Lorem ipsum dolor sit</h3><p>Short puppy bio text here</p><span class="btn">VOTE NOW</span></div>
      <div class="card"><div class="photo" role="img" aria-label="White puppy" style="background:linear-gradient(#f4f1ec,#d6cfc4)"></div><h3>Lorem ipsum dolor sit</h3><p>Short puppy bio text here</p><span class="btn">VOTE NOW</span></div>
      <svg class="arrow r" viewBox="0 0 10 16"><path d="M2 1l6 7-6 7" fill="none" stroke="currentColor" stroke-width="2"/></svg>
    </div>
    <div class="dots"><i class="on"></i><i></i><i></i><i></i></div>
  </div>
</section>

<section class="columns wrap">
  <div class="col popular">
    <h2>MOST PAWPULAR</h2>
    <ul>
      <li>Best chew toys for teething puppies</li>
      <li class="hot">Training your dog to walk on a loose leash</li>
      <li>Healthy treats dogs really love</li>
      <li>How to choose the right dog bed</li>
      <li>Top parks for dogs this summer</li>
    </ul>
    <div class="more">READ MORE...</div>
  </div>
  <div class="col news">
    <h2>LATEST NEWS</h2>
    <div class="item"><div class="date">12 Feb, 2015</div><h4>Lorem ipsum dolor sit amet</h4><p>New grooming guide for long haired breeds now live on the blog.</p></div>
    <div class="item"><div class="date">10 Feb, 2015</div><h4>Lorem ipsum dolor sit amet</h4><p>Spring photo contest opens soon, get your best shots ready.</p></div>
    <div class="item"><div class="date">07 Feb, 2015</div><h4>Lorem ipsum dolor sit amet</h4><p>Our expert answers your questions on puppy nutrition.</p></div>
    <div class="more">VIEW MORE...</div>
  </div>
  <div class="col testimonials">
    <h2>CLIENT TESTIMONIALS</h2>
    <div class="quote"><div class="avatar"></div><p>"A wonderful place to share tips with other owners. My dog and I have learned so much here." <b>Anna, Designer</b></p></div>
    <div class="quote"><div class="avatar"></div><p>"Great deals and honest reviews. I always check here before buying anything new." <b>Mark, Teacher</b></p></div>
    <div class="quote"><div class="avatar"></div><p>"The training videos helped our rescue settle into family life quickly." <b>Lucy, Manager</b></p></div>
    <div class="more">VIEW MORE...</div>
  </div>
</section>

<footer class="footer"><div class="wrap">
  <div class="fcol"><h5>Quick Links</h5><ul><li>Home</li><li>About Us</li><li>Contact Us</li><li>Dog Deals</li><li>Videos</li><li>Photos</li><li>Health</li></ul></div>
  <div class="fcol"><h5>Our Policies</h5><ul><li>Privacy Policy</li><li>Terms of Use</li><li>Returns</li><li>Shipping</li><li>FAQ</li></ul></div>
  <div class="fcol"><h5>My Account</h5><ul><li>Sign In</li><li>View Cart</li><li>My Wishlist</li><li>Track Order</li><li>Help</li></ul></div>
  <div class="fbrand">
    <div class="name">BrightKennels</div>
    <div class="call">CALL US NOW <b>555 014 2290</b></div>
    <div class="social"><i></i><i></i><i></i><i></i><i></i></div>
  </div>
</div></footer>
<div class="bottombar">© 2015 Bright Kennels. All rights reserved.</div>
</body>
</html>
```